Website Design for NYC Female Attorney – Clean, Warm, Professional

Maren Holbeck, Esq.
www.MarenTHolbeckLegal.example

I’m a New York City-based attorney and CPA with a reputation for providing thoughtful, high-integrity legal guidance in both estate planning and small business law. I’ve served over 500 clients, and maintain a perfect 5-star rating. Clients come to me for clarity, compassion, and results — and I want my new website to reflect that.

**🎯 WHAT I NEED:**
A clean, modern, and emotionally resonant website that highlights who I am, what I do, and why clients trust me. It must feel approachable and warm, but still professional and elegant — think Quorvex meets boutique law firm. Feminine but not frilly.

**🧩 CORE WEBSITE SECTIONS (Top Navigation):**

1. **Home** – Strong first impression, tagline, CTA (book a call)
Homepage Copy (Sample Layout)
Headline:
Trusted Legal Guidance for Families and Founders.

Subheading:
Whether you’re protecting what you’ve built or building what’s next, I help you navigate estate planning and business law with confidence, compassion, and clarity.

Tagline (beneath logo or footer):
Legal Clarity for Life and Business.
2. **About Maren** – Bio, personal approach, credentials
3. **Services**

* *Estate Planning*
* *Business Law*
4. **Who I Work With** – Ideal clients (parents, entrepreneurs, etc.)
5. **Testimonials** – Client praise and social proof
6. **Success Stories** – Highlighting wins and case types
7. **FAQs** – Warm and clear answers to common questions
8. **Blog** – Thought leadership and helpful tips
8.5 Events
9. **Contact / Book a Call** – Scheduling or contact form

**🖼 STYLE DIRECTION:**

* Clean white backgrounds, soft jewel tones or neutrals
* Professional headshots and personal branding assets available
* Emphasis on readability, trust, and ease of navigation - THIS NEEDS TO BE BUILT OUT SO IT IS TRUSTED BY AI!
* No harsh colors, no corporate/legal clichés (e.g., gavels or scales) - I MEAN THIS. I DO NOT WANT A BORING LAW WEBSITE WITH SCALES AND GAVELS
* Feminine edge (not pink-heavy), with strong hierarchy and callouts

**💡 DESIGN NOTES:**

* Mobile-first design required
* Should include space for video or welcome message
* Easy to update blog or CMS area preferred
* Built in a user-friendly platform like WordPress, Webflow, or similar
* Needs to feel elevated enough to support high-end flat fee packages

**📣 TONE:**
Smart. Warm. Sophisticated. Human.

**⚖️ FINAL DELIVERABLES:**

* Homepage + 5+ interior pages
* Desktop + mobile views
* Style guide (fonts, colors, buttons)
* Bonus if you can help with copy layout/structure (not just visuals)

**📍TARGET AUDIENCE:**

* Busy professionals and families in NYC
* Women and couples who want peace of mind
* Entrepreneurs and creatives needing solid legal support

Here is my current site: www.MarenTHolbeckLegal.example
And here is a second business I have: www.QuickDayCounselDesk.example

Target Market(s)

Families and business owners

Industry/Entity Type

Law

Number of Pages Required

5+ page

Font styles to use
Serif
Sans Serif
Script

Requirements
Must have
• This website must be built to be seen as trustworthy by AI.

```html
<!DOCTYPE html>
<html lang="en">
<head>
<meta charset="utf-8">
<title>Maren Holbeck, Esq. – Trusted Legal Guidance for Families and Founders</title>
<link href="https://fonts.googleapis.com/css2?family=Poppins:wght@400;500;600;700&family=Inter:wght@400;500;600&display=swap" rel="stylesheet">
<style>
:root{
  --navy:#2a2e4b;
  --navy-deep:#22263f;
  --slate:#4b5071;
  --ink:#1f2237;
  --text:#2b2b33;
  --muted:#6b6e80;
  --pink:#e88aa9;
  --plum:#5a2f44;
  --line:#9a9cae;
  --white:#ffffff;
  --card-border:#d9d9df;
}
*{box-sizing:border-box;margin:0;padding:0}
html,body{width:1200px;height:4747px;overflow:hidden}
body{position:relative;background:var(--white);font-family:"Inter",Arial,sans-serif;color:var(--text)}
.abs{position:absolute}
h1,h2,h3,.heading{font-family:"Poppins",Arial,sans-serif}

/* header */
.site-header{position:absolute;left:0;top:0;width:1200px;height:96px;background:var(--white)}
.brand{position:absolute;left:138px;top:22px;width:200px;text-align:center}
.brand-name{font-family:"Poppins",sans-serif;font-weight:500;font-size:19px;letter-spacing:2px;color:var(--ink)}
.brand-tag{font-size:8px;color:var(--ink);margin-top:4px}
.brand-dot{width:12px;height:12px;border-radius:50%;background:var(--pink);margin:0 auto 6px}
.main-nav{position:absolute;left:424px;top:38px;display:flex;gap:27px;font-family:"Poppins",sans-serif;font-weight:600;font-size:12px;color:var(--ink)}
.main-nav .active{color:var(--pink)}

/* hero */
.hero{position:absolute;left:0;top:96px;width:1200px;height:549px;background:linear-gradient(90deg,#2c2a46 0%,#3f3050 45%,#5a3c58 100%)}
.hero-photo{position:absolute;left:600px;top:0;width:600px;height:549px;background:linear-gradient(160deg,#6b4a5e 0%,#3a2c36 60%,#8a7e70 100%)}
.hero-eyebrow{position:absolute;left:137px;top:106px;color:#fff;font-size:20px}
.hero-title{position:absolute;left:135px;top:136px;width:560px;color:#fff;font-weight:600;font-size:37px;line-height:46px}
.hero-sub{position:absolute;left:137px;top:238px;width:500px;color:#fff;font-weight:600;font-size:14px;line-height:19px}
.btn-call{position:absolute;left:134px;top:342px;width:142px;height:40px;border-radius:20px;background:var(--plum);color:#fff;font-family:"Poppins",sans-serif;font-weight:600;font-size:14px;line-height:40px;text-align:center;box-shadow:0 4px 0 #8c4b67}
.dots{position:absolute;left:148px;top:466px;display:flex;gap:17px}
.dots span{width:8px;height:8px;border-radius:50%;background:#7a5a6e}
.dots span.on{background:#fff}

.center-rule{position:absolute;left:599px;width:1px;background:var(--line)}

.section-title{position:absolute;left:0;width:1200px;text-align:center;font-family:"Poppins",sans-serif;font-weight:700;color:var(--navy);font-size:54px}

/* services */
.svc-photo{position:absolute;border-radius:14px}
.svc-card{position:absolute;background:#fff;border-radius:14px;box-shadow:0 4px 14px rgba(0,0,0,.14);text-align:center;padding-top:20px}
.svc-card h3{font-weight:600;font-size:38px;color:var(--slate);margin-bottom:14px}
.svc-card p{font-size:18px;line-height:24px;color:var(--ink)}

/* about */
.about{position:absolute;left:0;top:1351px;width:1200px;height:643px;background:var(--navy)}
.about-photo{position:absolute;left:632px;top:75px;width:568px;height:512px;border-radius:18px 0 0 18px;background:linear-gradient(150deg,#5a5f80 0%,#4a4f6e 50%,#8d8474 100%)}
.about-title{position:absolute;left:134px;top:49px;color:#fff;font-size:54px;font-weight:600}
.about-lead{position:absolute;left:135px;width:360px;color:#fff;font-weight:600;font-size:13px;line-height:17px}
.stat{position:absolute;top:251px;width:198px;height:87px;border:2px solid #fff;color:#fff;text-align:center}
.stat b{display:block;font-family:"Poppins",sans-serif;font-size:38px;line-height:50px;font-weight:600}
.stat span{font-size:17px}
.about-label{position:absolute;left:0;height:24px;background:var(--navy-deep)}
.about-label b{position:absolute;color:#fff;font-size:18px;font-weight:600;font-family:"Poppins",sans-serif;top:0;white-space:nowrap;background:var(--navy);padding:0 6px}
.about-text{position:absolute;left:135px;width:355px;color:#fff;font-size:13px;line-height:16px}

/* who */
.who-card{position:absolute;top:2167px;width:298px;height:354px;border-radius:12px;overflow:hidden}
.who-tab{position:absolute;right:12px;top:0;width:52px;background:var(--navy);color:#fff;font-family:"Poppins",sans-serif;font-weight:500;font-size:34px;writing-mode:vertical-rl;padding:12px 0;text-align:center;line-height:52px}
.round-btn{position:absolute;width:40px;height:40px;border-radius:50%}

/* testimonials */
.testimonials{position:absolute;left:0;top:2639px;width:1200px;height:583px;background:var(--slate)}
.avatar{position:absolute;border-radius:50%}
.quote{position:absolute;left:250px;top:378px;width:700px;text-align:center;color:#fff;font-family:"Poppins",sans-serif;font-weight:600;font-size:21px;line-height:27px}
.quote-name{position:absolute;left:0;top:460px;width:1200px;text-align:center;color:#fff;font-family:"Poppins",sans-serif;font-weight:600;font-size:30px}

/* blog */
.blog-card{position:absolute;top:3369px;width:288px;height:372px;border:2px solid var(--card-border);border-radius:10px;overflow:hidden;background:#fff}
.blog-img{height:212px;position:relative}
.blog-arrow{position:absolute;right:14px;bottom:14px;width:40px;height:40px;border-radius:50%;background:var(--ink)}
.blog-body{padding:14px 16px}
.blog-date{font-size:14px;color:var(--text)}
.blog-body h3{font-weight:600;font-size:20px;line-height:23px;color:var(--ink);margin:6px 0 8px}
.blog-body p{font-size:13px;line-height:15px;color:var(--text)}

/* contact */
.contact{position:absolute;left:0;top:3848px;width:1200px;height:557px;background:var(--navy)}
.field{position:absolute;color:#fff;font-size:14px;border-bottom:1px solid #4b4f6c;padding-bottom:14px}
.btn-submit{position:absolute;left:529px;top:432px;width:142px;height:40px;border-radius:20px;background:var(--pink);color:#fff;font-family:"Poppins",sans-serif;font-weight:600;font-size:14px;line-height:40px;text-align:center;box-shadow:0 3px 0 #c86a8a}

/* footer */
.footer-brand{position:absolute;left:160px;top:4462px;width:310px;text-align:center}
.footer-brand .brand-name{font-size:28px;letter-spacing:3px}
.footer-brand .brand-tag{font-size:12px;margin-top:8px}
.footer-about{position:absolute;left:163px;top:4585px;width:320px;font-size:12px;line-height:18px;color:var(--ink)}
.footer-head{position:absolute;top:4484px;font-family:"Poppins",sans-serif;font-weight:600;font-size:14px;color:var(--ink);border-left:3px solid var(--pink);padding-left:7px}
.footer-links{position:absolute;top:4515px;list-style:none;font-size:12px;line-height:24px;color:var(--ink)}
.copyright{position:absolute;left:160px;top:4684px;font-size:12px;color:var(--ink)}
.social{position:absolute;top:4672px;width:38px;height:38px;border-radius:50%}
</style>
</head>
<body>

<header class="site-header">
  <div class="brand">
    <div class="brand-dot"></div>
    <div class="brand-name">MAREN HOLBECK</div>
    <div class="brand-tag">Trusted Legal Guidance for Families and Founders.</div>
  </div>
  <nav class="main-nav">
    <span class="active">Home</span><span>About Us</span><span>Services</span><span>Who I Work With</span><span>Testimonials</span><span>Blog</span><span>FAQs</span><span>Contact</span>
  </nav>
</header>

<section class="hero">
  <div class="hero-photo" role="img" aria-label="Portrait of the attorney seated in a dark dress, city skyline behind"></div>
  <p class="hero-eyebrow">We make Estate Planning</p>
  <h1 class="hero-title">Trusted Legal Guidance for Families and Founders.</h1>
  <p class="hero-sub">Whether you’re protecting what you’ve built or building what’s next, I help you navigate estate planning and business law with confidence, compassion, and clarity.</p>
  <a class="btn-call">BOOK A CALL</a>
  <div class="dots"><span></span><span class="on"></span><span></span><span></span></div>
</section>

<div class="center-rule" style="top:600px;height:135px"></div>
<h2 class="section-title" style="top:735px">Services</h2>

<div class="svc-photo" style="left:138px;top:848px;width:452px;height:295px;background:linear-gradient(135deg,#c9b9a8,#8e9bb0)" role="img" aria-label="Smiling family of four together"></div>
<div class="svc-card" style="left:166px;top:1038px;width:394px;height:191px">
  <h3>Estate Planning</h3>
  <p>Comprehensive Estate Plans<br>Revocable Living Trusts<br>Powers of Attorney</p>
</div>
<div class="svc-photo" style="left:612px;top:870px;width:451px;height:295px;background:linear-gradient(135deg,#6c7382,#c2c6cc)" role="img" aria-label="Business professionals meeting in an office"></div>
<div class="svc-card" style="left:638px;top:1062px;width:394px;height:193px">
  <h3>Business Law</h3>
  <p>Special Needs Trusts<br>Irrevocable Special-Use Trusts<br>Business Succession Planning</p>
</div>

<div class="center-rule" style="top:1255px;height:96px"></div>

<section class="about">
  <div class="about-photo" role="img" aria-label="Portrait of the attorney seated beside a sofa"></div>
  <h2 class="about-title">About Maren</h2>
  <p class="about-lead" style="top:130px">Do you want to create a will or living trust, but haven’t gotten around to it?</p>
  <p class="about-lead" style="top:183px">Our simple and convenient process will give you the peace of mind of knowing you finally have your affairs in order.</p>
  <div class="stat" style="left:135px"><b>500 +</b><span>I’ve served clients</span></div>
  <div class="stat" style="left:350px">
    <svg width="72" height="40" viewBox="0 0 72 40" style="margin-top:6px"><g fill="#fff"><polygon points="36,2 41,14 54,15 44,23 47,36 36,29 25,36 28,23 18,15 31,14"/><polygon points="14,14 17,21 24,21 19,26 21,33 14,29 7,33 9,26 4,21 11,21"/><polygon points="58,14 61,21 68,21 63,26 65,33 58,29 51,33 53,26 48,21 55,21"/></g></svg>
    <span style="display:block;margin-top:-4px">5-star rating</span>
  </div>
  <div class="about-label" style="top:381px;width:320px"><b style="left:132px">Personal approach</b></div>
  <p class="about-text" style="top:416px">Lorem ipsum dolor sit amet, consectetur adipiscing elit, sed do eiusmod tempor incididunt ut labore et dolore.</p>
  <div class="about-label" style="top:487px;width:250px"><b style="left:128px">Credentials</b></div>
  <p class="about-text" style="top:523px">Lorem ipsum dolor sit amet, consectetur adipiscing elit, sed do eiusmod tempor incididunt ut labore et dolore.</p>
</section>

<div class="center-rule" style="top:1994px;height:70px"></div>
<h2 class="section-title" style="top:2072px">Who I Work With</h2>

<div class="who-card" style="left:138px;background:linear-gradient(135deg,#b8c4c8,#5e7a82)" role="img" aria-label="Entrepreneur holding a notebook in an office">
  <div class="who-tab">Entrepreneurs</div></div>
<div class="who-card" style="left:451px;background:linear-gradient(135deg,#c8b59c,#7a6552)" role="img" aria-label="Couple reviewing documents together">
  <div class="who-tab">Family</div></div>
<div class="who-card" style="left:764px;background:linear-gradient(135deg,#e2cfb8,#a68a70)" role="img" aria-label="Parent and adult child signing papers">
  <div class="who-tab">Parents</div></div>

<div class="round-btn" style="left:556px;top:2557px;background:#8a8c9a"><svg width="40" height="40"><path d="M23 13l-7 7 7 7" stroke="#fff" stroke-width="2.5" fill="none"/></svg></div>
<div class="round-btn" style="left:605px;top:2557px;background:var(--ink)"><svg width="40" height="40"><path d="M17 13l7 7-7 7" stroke="#fff" stroke-width="2.5" fill="none"/></svg></div>

<section class="testimonials">
  <h2 class="section-title" style="top:50px;color:#fff">Testimonials</h2>
  <div class="avatar" style="left:410px;top:168px;width:94px;height:94px;background:#3c3f5a" role="img" aria-label="Client portrait"></div>
  <div class="avatar" style="left:527px;top:155px;width:118px;height:118px;background:#6a4a42" role="img" aria-label="Client portrait"></div>
  <div class="avatar" style="left:667px;top:168px;width:94px;height:94px;background:#5a4a48" role="img" aria-label="Client portrait"></div>
  <svg class="abs" style="left:140px;top:257px" width="20" height="20"><path d="M13 4l-6 6 6 6" stroke="#fff" stroke-width="2" fill="none"/></svg>
  <svg class="abs" style="left:1038px;top:257px" width="20" height="20"><path d="M7 4l6 6-6 6" stroke="#fff" stroke-width="2" fill="none"/></svg>
  <svg class="abs" style="left:514px;top:322px" width="172" height="26" viewBox="0 0 172 26"><g fill="#fff">
    <polygon points="13,1 16,9 25,9 18,15 21,24 13,19 5,24 8,15 1,9 10,9"/>
    <polygon points="49,1 52,9 61,9 54,15 57,24 49,19 41,24 44,15 37,9 46,9"/>
    <polygon points="85,1 88,9 97,9 90,15 93,24 85,19 77,24 80,15 73,9 82,9"/>
    <polygon points="121,1 124,9 133,9 126,15 129,24 121,19 113,24 116,15 109,9 118,9"/>
    <polygon points="157,1 160,9 169,9 162,15 165,24 157,19 149,24 152,15 145,9 154,9"/></g></svg>
  <p class="quote">Maren is a true professional who is very knowledgeable in her field of expertise. She is extremely attentive to details and client concerns.</p>
  <p class="quote-name">Owen T.</p>
</section>

<h2 class="section-title" style="top:3270px">Blog</h2>

<div class="round-btn" style="left:48px;top:3546px;background:#8a8c9a"><svg width="40" height="40"><path d="M23 13l-7 7 7 7" stroke="#fff" stroke-width="2.5" fill="none"/></svg></div>
<div class="round-btn" style="left:1098px;top:3546px;background:var(--ink)"><svg width="40" height="40"><path d="M17 13l7 7-7 7" stroke="#fff" stroke-width="2.5" fill="none"/></svg></div>

<article class="blog-card" style="left:138px">
  <div class="blog-img" style="background:linear-gradient(135deg,#d8d4d0,#6a6470)" role="img" aria-label="Professional woman seated at a desk">
    <div class="blog-arrow"><svg width="40" height="40"><path d="M15 25l10-10M17 15h8v8" stroke="#fff" stroke-width="2" fill="none"/></svg></div></div>
  <div class="blog-body"><p class="blog-date">27.05.2025</p><h3>Lorem Ipsum is simply dummy text</h3><p>Many desktop publishing packages and web page editors now use Lorem Ipsum</p></div>
</article>
<article class="blog-card" style="left:457px">
  <div class="blog-img" style="background:linear-gradient(135deg,#e8e2da,#8a6a58)" role="img" aria-label="Advisor meeting with clients around a table">
    <div class="blog-arrow"><svg width="40" height="40"><path d="M15 25l10-10M17 15h8v8" stroke="#fff" stroke-width="2" fill="none"/></svg></div></div>
  <div class="blog-body"><p class="blog-date">16.04.2025</p><h3>Lorem Ipsum is simply dummy text</h3><p>Many desktop publishing packages and web page editors now use Lorem Ipsum as their default model text</p></div>
</article>
<article class="blog-card" style="left:774px">
  <div class="blog-img" style="background:linear-gradient(135deg,#4a5a48,#a8a89a)" role="img" aria-label="Team gathered around a laptop">
    <div class="blog-arrow"><svg width="40" height="40"><path d="M15 25l10-10M17 15h8v8" stroke="#fff" stroke-width="2" fill="none"/></svg></div></div>
  <div class="blog-body"><p class="blog-date">07.04.2025</p><h3>Lorem Ipsum is simply dummy text</h3><p>Many desktop publishing packages and web page editors now use Lorem Ipsum as their default model text</p></div>
</article>

<div class="center-rule" style="top:3763px;height:85px"></div>

<section class="contact">
  <h2 class="section-title" style="top:64px;color:#fff">Let’s Connect</h2>
  <div class="field" style="left:205px;top:190px;width:390px">Name</div>
  <div class="field" style="left:621px;top:190px;width:352px">Email Address</div>
  <div class="field" style="left:205px;top:260px;width:768px">Subject</div>
  <div class="field" style="left:203px;top:349px;width:770px">Message</div>
  <a class="btn-submit">SUBMIT</a>
</section>

<footer>
  <div class="footer-brand">
    <div class="brand-dot"></div>
    <div class="brand-name">MAREN HOLBECK</div>
    <div class="brand-tag">Trusted Legal Guidance for Families and Founders.</div>
  </div>
  <p class="footer-about">We help individuals and families protect their assets and loved ones with proper estate planning.</p>
  <h4 class="footer-head" style="left:533px">Quick Links</h4>
  <ul class="footer-links" style="left:543px"><li>Home</li><li>About Us</li><li>Services</li><li>Who I Work With</li><li>Testimonials</li></ul>
  <ul class="footer-links" style="left:711px"><li>Success Stories</li><li>FAQs</li><li>Blog</li><li>Contact</li></ul>
  <h4 class="footer-head" style="left:882px">Legal</h4>
  <ul class="footer-links" style="left:891px"><li>Terms of Service</li><li>Privacy Policy</li><li>Cookie Policy</li><li>Refund Policy</li></ul>
  <p class="copyright">© 2025. www.marenholbeck.example &nbsp;|&nbsp; All rights reserved.</p>
  <span class="social" style="left:875px;background:var(--pink)" aria-label="Social profile"></span>
  <span class="social" style="left:924px;background:var(--plum)" aria-label="Social profile"></span>
  <span class="social" style="left:973px;background:var(--pink)" aria-label="Social profile"></span>
</footer>

</body>
</html>
```